POLITICAL CARD TO HAND OUT

A LITTLE LARGER THAN THE REGULAR BUSINESS CARD WITH THE ABOVE INFORMATION.

Industry/Entity Type

Business

Contact Information for Business Card

ELECT *DEAN HOLT* FOR JUSTICE OF THE PEACE PCT 6-EXPERIENCED LEADERSHIP- WITH MY PICTURE ON IT- PHONE 347-610-2853-MERIDIAN PRIMARY - EARLY VOTING FEB 18TH THRU FEB 28 AND ELECTION DAY IS MARCH 4TH, 2014- USE RED WHITE AND BLUE WITH SOME STARS.

Requirements
Must have
• A FIVE POINTED STAR ON EACH SIDE OF MY NAME

```html
<!DOCTYPE html>
<html lang="en">
<head>
<meta charset="utf-8">
<title>Elect Dean Holt – Justice of the Peace Pct 6</title>
<link rel="stylesheet" href="https://fonts.googleapis.com/css2?family=Bodoni+Moda:wght@700;900&display=swap">
<style>
  :root {
    --blue-deep: #1f4f9c;
    --blue-mid: #2d6cc4;
    --blue-light: #5a93dc;
    --red: #d4262b;
    --red-dark: #b81a20;
    --white: #ffffff;
    --photo-dark: #3a3532;
    --photo-light: #8e8a86;
    --page: #e9e9e9;
  }
  * { margin: 0; padding: 0; box-sizing: border-box; }
  html, body {
    width: 1200px; height: 575px; overflow: hidden;
    background: var(--page);
  }
  .card {
    position: relative;
    width: 1200px; height: 575px;
    overflow: hidden;
    font-family: "Bodoni Moda", "Times New Roman", serif;
    color: var(--white);
    background: linear-gradient(160deg, var(--blue-light) 0%, var(--blue-mid) 40%, var(--blue-deep) 100%);
  }
  .flag-field {
    position: absolute; left: 0; top: 0;
    width: 330px; height: 200px;
    background: linear-gradient(135deg, #2a5bb0 0%, #4f84d2 60%, rgba(90,147,220,0) 100%);
  }
  .candidate-photo {
    position: absolute; left: 50px; top: 30px;
    width: 370px; height: 370px;
    background: radial-gradient(ellipse at 50% 35%, var(--photo-light) 0%, var(--photo-dark) 75%);
  }
  .headline {
    position: absolute; left: 440px; top: 18px; width: 730px;
    text-align: center;
  }
  .elect {
    font-size: 112px; font-weight: 900; letter-spacing: 18px; line-height: 1;
  }
  .name {
    display: flex; align-items: center; justify-content: center; gap: 16px;
    font-size: 78px; font-weight: 900; letter-spacing: 8px; line-height: 1;
    margin-top: 6px;
  }
  .name-star { width: 34px; height: 34px; fill: var(--white); }
  .rule {
    height: 4px; background: var(--white); margin: 14px 10px 10px;
  }
  .office {
    font-size: 46px; font-weight: 700; line-height: 1.05; letter-spacing: 1px;
  }
  .tagline {
    font-size: 38px; font-weight: 700; line-height: 1.1; letter-spacing: 1px;
  }
  .ballot-band {
    position: absolute; left: 0; bottom: 0;
    width: 1200px; height: 170px;
    background: linear-gradient(180deg, var(--red) 0%, var(--red-dark) 100%);
    border-top: 6px solid var(--white);
    padding: 10px 24px 0;
  }
  .phone-line {
    font-size: 44px; font-weight: 900; line-height: 1; white-space: nowrap;
  }
  .voting-dates {
    font-size: 23px; font-weight: 700; line-height: 1.3; margin-top: 6px; white-space: nowrap;
    letter-spacing: 0.5px;
  }
  .star-row {
    position: absolute; left: 0; bottom: 10px; width: 1200px; height: 44px;
  }
  .star-row use { fill: var(--white); }
</style>
</head>
<body>
<main class="card">
  <svg width="0" height="0" style="position:absolute">
    <defs>
      <symbol id="star" viewBox="0 0 100 100">
        <polygon points="50,3 61,38 98,38 68,60 79,95 50,73 21,95 32,60 2,38 39,38"/>
      </symbol>
    </defs>
  </svg>

  <div class="flag-field" role="img" aria-label="Waving American flag with stars in the upper corner"></div>
  <div class="candidate-photo" role="img" aria-label="Portrait of the candidate in a white cowboy hat, dark suit and tie"></div>

  <header class="headline">
    <div class="elect">ELECT</div>
    <div class="name">
      <svg class="name-star" aria-hidden="true"><use href="#star"/></svg>
      <span>DEAN HOLT</span>
      <svg class="name-star" aria-hidden="true"><use href="#star"/></svg>
    </div>
    <div class="rule"></div>
    <div class="office">FOR JUSTICE<br>OF THE PEACE PCT 6</div>
    <div class="tagline">EXPERIENCED LEADERSHIP</div>
  </header>

  <section class="ballot-band">
    <p class="phone-line">PHONE 347-610-2853-MERIDIAN PRIMARY</p>
    <p class="voting-dates">EARLY VOTING FEB 18TH THRU FEB 28 AND ELECTION DAY IS MARCH 4TH, 2014</p>
    <svg class="star-row" viewBox="0 0 1200 44" aria-hidden="true">
      <use href="#star" x="14" y="4" width="36" height="36"/>
      <use href="#star" x="80" y="4" width="36" height="36"/>
      <use href="#star" x="146" y="4" width="36" height="36"/>
      <use href="#star" x="212" y="4" width="36" height="36"/>
      <use href="#star" x="278" y="4" width="36" height="36"/>
      <use href="#star" x="344" y="4" width="36" height="36"/>
      <use href="#star" x="410" y="4" width="36" height="36"/>
      <use href="#star" x="476" y="4" width="36" height="36"/>
      <use href="#star" x="542" y="4" width="36" height="36"/>
      <use href="#star" x="608" y="4" width="36" height="36"/>
      <use href="#star" x="674" y="4" width="36" height="36"/>
      <use href="#star" x="740" y="4" width="36" height="36"/>
      <use href="#star" x="806" y="4" width="36" height="36"/>
      <use href="#star" x="872" y="4" width="36" height="36"/>
      <use href="#star" x="938" y="4" width="36" height="36"/>
      <use href="#star" x="1004" y="4" width="36" height="36"/>
      <use href="#star" x="1070" y="4" width="36" height="36"/>
      <use href="#star" x="1136" y="4" width="36" height="36"/>
    </svg>
  </section>
</main>
</body>
</html>
```